Website Redesign for an Appointment Setting and Lead Generation Company.

I need to redesign an existing website. The website that we are looking to be redesigned is www.palvorintel.com. PalvorIntel is a B2B appointment setting organization. The idea is to present a modern look website for professional services company. The idea is to engage the user, look at various services and generate more inbound leads for the website

Target Market(s)

US, APAC, Europe, UK. Focused on B2B companies more than $100 Mn

Industry/Entity Type

Professional Service

Number of Pages Required

5+ page

Font styles to use
Other font styles liked:
• Roboto

Requirements
Must have
• Home Page - Banner Image, Section for Client testimonials
Industry Page - To show industry capabilities
Services Page - To show service capabilities
Blogs Page - to show blogs
Offerings Page - Offerings Page
Nice to have
• I would like to have a elegant design with small animation. Preferably use colors from the logo attached. Use infographics where possible

```html
<!DOCTYPE html>
<html lang="en">
<head>
<meta charset="utf-8">
<title>PalvorIntel – B2B Appointment Setting &amp; Lead Generation</title>
<link href="https://fonts.googleapis.com/css2?family=Roboto:wght@300;400;500;700&display=swap" rel="stylesheet">
<style>
:root{
  --red:#d8343a;
  --red-soft:#e0494e;
  --ink:#222;
  --text:#444;
  --muted:#666;
  --topbar:#151515;
  --dark:#2f2f2f;
  --footer:#262626;
  --light:#f3f3f3;
  --line:#d9d9d9;
  --teal:#3fd8be;
  --blue:#27aee0;
  --yellow:#fbbd12;
  --pink:#f1306e;
}
*{box-sizing:border-box;margin:0;padding:0}
html,body{width:1200px;height:3847px;overflow:hidden}
body{font-family:'Roboto',sans-serif;color:var(--text);background:#fff;position:relative}
.abs{position:absolute}
a{color:inherit;text-decoration:none}

.topbar{left:0;top:0;width:1200px;height:42px;background:var(--topbar);color:#ddd;font-size:11px}
.topbar .info{position:absolute;left:133px;top:14px;display:flex;gap:22px}
.topbar .info span{display:flex;align-items:center;gap:7px}
.topbar svg{width:11px;height:11px}
.topbar .social{position:absolute;right:133px;top:12px;display:flex;gap:8px}
.dot{width:17px;height:17px;border-radius:50%;background:#666;display:inline-block}
.topbar .social .dot{width:16px;height:16px}

.hero{left:0;top:42px;width:1200px;height:515px;background:linear-gradient(120deg,#4a3a33 0%,#6b5647 40%,#564a44 70%,#3b3431 100%)}
.hero-inner{left:0;top:0;width:1200px;height:515px;background:linear-gradient(90deg,rgba(30,20,15,.55),rgba(30,20,15,.15))}
.nav{left:133px;top:0;width:933px;height:70px;background:#fff;display:flex;align-items:center;padding:0 14px}
.brand{display:flex;align-items:center;gap:8px;font-size:25px;font-weight:500;color:var(--red)}
.brand .sq{width:22px;height:22px;background:var(--red)}
.nav ul{list-style:none;display:flex;gap:27px;margin-left:auto;margin-right:30px;font-size:10.5px;font-weight:500;color:var(--ink)}
.nav li.on{color:var(--red);border-bottom:1px solid var(--red);padding-bottom:3px}
.nav .search{width:30px;height:30px;background:var(--red);display:flex;align-items:center;justify-content:center}
.hero h1{left:166px;top:183px;font-size:36px;line-height:42px;font-weight:500;color:var(--red)}
.hero p{left:167px;top:283px;width:440px;font-size:12px;line-height:15px;color:#fff}
.btn-red{background:var(--red);color:#fff;font-size:11.5px;font-weight:500;display:flex;align-items:center;justify-content:center}
.hero .btn-red{left:167px;top:359px;width:109px;height:32px}
.hero .pager{left:1058px;top:268px;display:flex;flex-direction:column;gap:13px}
.hero .pager i{width:7px;height:7px;border-radius:50%;background:#eee;display:block}
.hero .pager i.on{background:var(--red)}

.offer-img{left:133px;top:619px;width:377px;height:296px;background:linear-gradient(135deg,#c8c0b6,#7f7a75 60%,#454547)}
.offer-text{left:564px;top:628px;width:470px}
.h-red{color:var(--red);font-weight:500}
.offer-text h2{font-size:24px;line-height:29px}
.offer-text p{font-size:11px;line-height:16.5px;margin-top:18px;color:var(--text)}
.offer-text h2+p{margin-top:24px}
.btn-line{border:1px solid #999;color:var(--ink);font-size:11px;display:inline-flex;align-items:center;justify-content:center}
.offer-text .btn-line{width:98px;height:30px;margin-top:26px}

.card{top:942px;width:297px;height:236px;background:#fff;box-shadow:0 2px 10px rgba(0,0,0,.12);z-index:2}
.card .ph{height:130px}
.card .ico{position:absolute;left:20px;top:110px;width:38px;height:38px;background:var(--red);display:flex;align-items:center;justify-content:center}
.card h3{position:absolute;left:20px;top:165px;font-size:14.5px;font-weight:500;color:var(--ink)}
.card p{position:absolute;left:20px;top:190px;width:230px;font-size:10.5px;line-height:14px;color:var(--muted)}
.card.red{background:var(--red)}
.card.red .ico{background:#fff}
.card.red h3{top:105px;color:#fff}
.card.red p{top:130px;width:255px;color:#fff;font-size:10.5px;line-height:15px}
.card.red .ph{height:72px;background:linear-gradient(90deg,#e9e1e3,#c3c9d3)}

.stats{left:0;top:1161px;width:1200px;height:396px;background:var(--dark)}
.stats h2{position:absolute;left:133px;top:87px;width:360px;font-size:30px;line-height:40px;color:#fff;font-weight:500}
.stats h2 em{font-style:normal;color:var(--red)}
.stat{position:absolute;width:159px;height:105px;background:#fff;padding:14px 14px}
.stat b{display:block;font-size:27px;font-weight:500;color:var(--red)}
.stat span{display:block;font-size:11px;line-height:13px;color:var(--text);margin-top:12px}

.testi{left:0;top:1557px;width:1200px;height:265px;text-align:center}
.testi h2{position:absolute;left:0;width:1200px;top:43px;font-size:25px}
.testi p{position:absolute;left:250px;width:700px;top:101px;font-size:11px;line-height:17px;color:var(--text)}
.testi .who{position:absolute;left:0;width:1200px;top:187px;font-size:11px;line-height:17px;color:var(--ink)}
.arrow-btn{position:absolute;top:130px;width:38px;height:38px;border:1px solid #ccc;display:flex;align-items:center;justify-content:center;background:#fff}

.rank{left:0;top:1822px;width:590px;height:396px;background:var(--red);color:#fff}
.rank h2{position:absolute;left:133px;top:38px;font-size:22px;line-height:28px;font-weight:500}
.acc{position:absolute;left:133px;width:377px;height:33px;background:var(--red-soft);display:flex;align-items:center;justify-content:space-between;padding:0 20px;font-size:12.5px;font-weight:500}
.acc i{width:17px;height:17px;border-radius:50%;background:#fff;color:var(--red);font-style:normal;font-size:13px;display:flex;align-items:center;justify-content:center;line-height:1}
.rank ul{position:absolute;left:153px;top:164px;list-style:none;font-size:11px;line-height:23px}
.rank li::before{content:"→ ";}
.leads{left:590px;top:1822px;width:610px;height:396px;background:linear-gradient(135deg,#3a3a3a,#222 60%,#303030)}
.leads h2{position:absolute;left:0;width:610px;text-align:center;top:38px;font-size:22px;line-height:28px;color:#fff;font-weight:500}
.leads h2 em{font-style:normal;color:var(--red)}
.lbox{position:absolute;width:159px;height:91px;background:#fff;padding:16px 14px}
.lbox b{display:block;font-size:26px;font-weight:500;color:var(--red)}
.lbox span{display:block;font-size:11px;font-weight:500;color:var(--ink);margin-top:8px}

.cap h2{left:133px;top:2268px;font-size:25px;line-height:28px}
.cap .body{left:133px;top:2364px;width:500px;font-size:10.5px;line-height:16.5px}
.cap .body p+p{margin-top:18px}
.legend{position:absolute;top:2528px;width:140px;font-size:10.5px;line-height:14.5px;color:var(--text)}
.legend .k{display:flex;align-items:center;gap:12px;font-weight:500;margin-bottom:12px}
.legend .k i{width:17px;height:17px;display:block}
.pie{left:728px;top:2290px}

.blogs{left:0;top:2669px;width:1200px;height:436px;background:var(--light)}
.blogs h2{position:absolute;left:0;width:1200px;text-align:center;top:48px;font-size:25px}
.blogs .view{position:absolute;left:979px;top:47px;width:88px;height:28px;background:#fff;gap:8px}
.post{position:absolute;top:113px;width:297px;text-align:center}
.post .ph{height:187px}
.post h3{font-size:12px;line-height:17px;font-weight:500;color:var(--ink);margin:20px auto 0;width:240px}
.post .btn-line{width:97px;height:27px;margin-top:10px;border-color:#ccc;background:#fff}

.foot-bg{left:0;top:3490px;width:1200px;height:357px;background:var(--footer)}
.form{left:185px;top:3161px;width:490px;height:366px;background:#fff;box-shadow:0 2px 14px rgba(0,0,0,.15)}
.form h2{position:absolute;left:20px;top:42px;font-size:21px;font-weight:400;color:var(--ink)}
.fld{position:absolute;height:37px;border:1px solid var(--line);font-size:10.5px;color:#999;padding:0 14px;display:flex;align-items:center;justify-content:space-between}
.form .btn-red{position:absolute;left:20px;top:298px;width:102px;height:34px}
.map{left:675px;top:3161px;width:340px;height:366px;background:linear-gradient(160deg,#eef0f2,#e3e8ea 60%,#dfe6e1)}

.fcol{position:absolute;top:3572px;font-size:11px;line-height:20px;color:#ddd}
.fcol h4{font-size:15px;font-weight:500;color:var(--red);margin-bottom:12px}
.fcol ul{list-style:none}
.fcol li::before{content:"→ ";color:#ccc}
.fcol li.on{color:var(--red)}
.fbrand{position:absolute;left:133px;top:3578px;display:flex;align-items:center;gap:8px;color:#fff;font-size:17px;font-weight:500}
.fbrand .sq{width:20px;height:20px;background:var(--red)}
.fabout{position:absolute;left:133px;top:3645px;width:125px;font-size:11px;line-height:16px;color:#ddd}
.fsocial{position:absolute;left:133px;top:3715px;display:flex;gap:11px}
.fsocial .dot{background:#ddd}
.crow{display:flex;gap:14px;align-items:flex-start;margin-bottom:16px}
.copy{left:0;top:3806px;width:1200px;height:41px;background:var(--red);color:#fff;font-size:10.5px;display:flex;align-items:center;justify-content:center}
</style>
</head>
<body>

<div class="abs topbar">
  <div class="info">
    <span><svg viewBox="0 0 12 12"><circle cx="6" cy="6" r="5.5" fill="#d8343a"/><path d="M6 3v3l2 1" stroke="#fff" fill="none"/></svg>07:00 AM - 12:00 PM</span>
    <span><svg viewBox="0 0 12 12"><rect x="0.5" y="2" width="11" height="8" fill="#d8343a"/><path d="M1 2.5l5 4 5-4" stroke="#fff" fill="none"/></svg>info@palvorintel.com</span>
    <span><svg viewBox="0 0 12 12"><path d="M2 1l2.5 0 1 3-1.5 1a6 6 0 0 0 3 3l1-1.5 3 1v2.5A1 1 0 0 1 10 11 9 9 0 0 1 1 2a1 1 0 0 1 1-1z" fill="#d8343a"/></svg>555.214.7730</span>
  </div>
  <div class="social"><i class="dot"></i><i class="dot"></i><i class="dot"></i><i class="dot"></i></div>
</div>

<section class="abs hero">
  <div class="abs hero-inner" role="img" aria-label="Team of colleagues pointing at financial report charts on a desk"></div>
  <nav class="abs nav">
    <div class="brand"><span class="sq"></span>PalvorIntel</div>
    <ul>
      <li class="on">HOME</li><li>ABOUT</li><li>SERVICES</li><li>OUR EXPERTISE</li><li>LIBRARY</li><li>CONTACT US</li>
    </ul>
    <div class="search"><svg width="12" height="12" viewBox="0 0 12 12"><circle cx="5" cy="5" r="3.6" stroke="#fff" stroke-width="1.4" fill="none"/><path d="M7.7 7.7l3 3" stroke="#fff" stroke-width="1.4"/></svg></div>
  </nav>
  <h1 class="abs">Build your Sales Pipeline<br>in the New Normal!</h1>
  <p class="abs">Providing end-to-end webinar management services - including platform support, audience acquisition, providing subject matter expert speakers, webinar moderation, reporting, and lead nurturing on the webinar attendees</p>
  <a class="abs btn-red">Know More</a>
  <div class="abs pager"><i></i><i class="on"></i><i></i></div>
</section>

<div class="abs offer-img" role="img" aria-label="Business team smiling and discussing around a laptop"></div>
<div class="abs offer-text">
  <h2 class="h-red">Offering Dynamic Solutions for<br>your Niche Product Offerings</h2>
  <p>Ranked amongst the best B2B lead generation companies globally we have our presence across North America, Europe, APAC and India.</p>
  <p>Our experienced and trained lead generation executives understand your unique service offerings and work along your campaign journey to achieve the desired goals.</p>
  <p>Leveraging our extensive proprietary database, we target key decision-makers &amp; influencers across industries.</p>
  <a class="btn-line">Read More</a>
</div>

<div class="abs card" style="left:133px">
  <div class="ph" role="img" aria-label="Hand holding a glowing globe" style="background:linear-gradient(135deg,#0d1a3a,#2a5aa0 55%,#101426)"></div>
  <div class="ico"><svg width="22" height="22" viewBox="0 0 22 22" fill="none" stroke="#fff" stroke-width="1.4"><circle cx="11" cy="11" r="9"/><ellipse cx="11" cy="11" rx="4" ry="9"/><path d="M2 11h18M4 6h14M4 16h14"/></svg></div>
  <h3>Global Partner</h3>
  <p>With Delivery locations across 4 countries, PalvorIntel is one of the top lead...</p>
</div>
<div class="abs card" style="left:451px">
  <div class="ph" role="img" aria-label="Executives in a meeting around a conference table" style="background:linear-gradient(135deg,#e6e9ee,#9ea6b2 60%,#4c5462)"></div>
  <div class="ico"><svg width="22" height="22" viewBox="0 0 22 22" fill="none" stroke="#fff" stroke-width="1.4"><circle cx="11" cy="11" r="3.5"/><path d="M11 1.5v3M11 17.5v3M1.5 11h3M17.5 11h3M4.3 4.3l2.1 2.1M15.6 15.6l2.1 2.1M4.3 17.7l2.1-2.1M15.6 6.4l2.1-2.1"/><circle cx="11" cy="11" r="6.5"/></svg></div>
  <h3>Doming Expertise</h3>
  <p>With Delivery locations across 4 countries, PalvorIntel is one of the top lead...</p>
</div>
<div class="abs card red" style="left:769px">
  <div class="ph" role="img" aria-label="Digital network of connected business icons"></div>
  <div class="ico" style="top:48px;width:38px;height:38px"><svg width="22" height="22" viewBox="0 0 22 22" fill="none" stroke="#d8343a" stroke-width="1.4"><circle cx="11" cy="11" r="9"/><ellipse cx="11" cy="11" rx="4" ry="9"/><path d="M2 11h18M4 6h14M4 16h14"/></svg></div>
  <h3>Proprietary Systems</h3>
  <p>Our unique &amp; proprietary Reach PRIME Model, powered by in house researched database of more than 750K Influencers and Decision makers enables us to reach out to your targeted clients to setup appointments</p>
</div>

<section class="abs stats">
  <h2>Let your Sales Team<br>focus on Closures with<br>our <em>B2B Lead</em><br>Generation Services</h2>
  <div class="stat" style="left:548px;top:94px"><b>3800</b><span>Research Reports<br>Generated</span></div>
  <div class="stat" style="left:727px;top:94px"><b>80%</b><span>Client Retention<br>Rate</span></div>
  <div class="stat" style="left:907px;top:94px"><b>500+</b><span>Surveys and Interviews<br>conducted per month</span></div>
  <div class="stat" style="left:548px;top:221px"><b>50%</b><span>Leads Generated<br>with CXOs &amp; VPs</span></div>
  <div class="stat" style="left:727px;top:221px"><b>33</b><span>Events<br>Managed</span></div>
  <div class="stat" style="left:907px;top:221px"><b>20</b><span>Databases<br>Subscribed</span></div>
</section>

<section class="abs testi">
  <h2 class="h-red">Testimonial</h2>
  <div class="arrow-btn" style="left:133px"><svg width="12" height="10" viewBox="0 0 12 10" fill="none" stroke="#999" stroke-width="1.3"><path d="M11 5H1M5 1L1 5l4 4"/></svg></div>
  <p>I used PI in Q4 2016 and look forward to continuing the great work they began. My experience with PalvorIntel has been exceptional. Within two months they showed impressive and immediate results helping achieve our sales pipeline goals. PalvorIntel knowledge and experience in the technology marketplace is really strong. The team is great to work with and brings a tremendous value add to our organization. We have found a true partner in PalvorIntel for our B2B lead generation needs.</p>
  <div class="who">Client Director<br>Vice President Decision Analytics – Leading Digital Intelligence company</div>
  <div class="arrow-btn" style="left:1029px;border-color:var(--red)"><svg width="12" height="10" viewBox="0 0 12 10" fill="none" stroke="#d8343a" stroke-width="1.3"><path d="M1 5h10M7 1l4 4-4 4"/></svg></div>
</section>

<section class="abs rank">
  <h2>Ranked amongst the top B2B Lead<br>Generation Companies across The Globe</h2>
  <div class="acc" style="top:117px">North America<i>−</i></div>
  <ul>
    <li>Delivery Centre in California</li>
    <li>Multiple Sales Offices Across US</li>
    <li>CAN-SPAM Compliant Process</li>
    <li>End-to-End Event Execution Capabilities</li>
  </ul>
  <div class="acc" style="top:272px">Europe &amp; UK<i>+</i></div>
  <div class="acc" style="top:316px">APAC<i>+</i></div>
</section>
<section class="abs leads" role="img" aria-label="Dark chessboard background with chess pieces">
  <h2><em>12000+</em> Leads Generated<br>in Last 10 Months</h2>
  <div class="lbox" style="left:80px;top:137px"><b>45%</b><span>North America</span></div>
  <div class="lbox" style="left:259px;top:137px"><b>35%</b><span>UK/EMEA</span></div>
  <div class="lbox" style="left:80px;top:249px"><b>15%</b><span>APAC &amp; ANZ</span></div>
  <div class="lbox" style="left:259px;top:249px"><b>5%</b><span>Rest of the World</span></div>
</section>

<section class="cap">
  <h2 class="abs h-red">Leading-edge Capabilities for your<br>Competitive Offerings</h2>
  <div class="abs body">
    <p>As the needs of your clients evolve, so should your service offerings. Our capabilities boost your sales pipeline for global outreach and give you an edge over your competitors. To understand your prospects' needs and your service offerings, PalvorIntel' executives are regularly trained on domains and next-generation service offerings.</p>
    <p>Our capabilities include delivering campaigns in local languages across continents &amp; expertise in next-gen offerings like ML/AI/RPA. This is a testament based on the campaigns we delivered in the last one year.</p>
  </div>
  <div class="legend" style="left:133px;width:130px"><div class="k"><i style="background:var(--teal)"></i><span style="color:var(--teal)">75%</span></div>Multilingual Campaigns Executed by Onsite Resources</div>
  <div class="legend" style="left:293px;width:135px"><div class="k"><i style="background:var(--blue)"></i><span style="color:var(--blue)">50%</span></div>Campaigns on Traditional IT &amp; Infrastructure Management Services</div>
  <div class="legend" style="left:452px;width:140px"><div class="k"><i style="background:var(--yellow)"></i><span style="color:var(--yellow)">20%</span></div>Campaigns on AI/ML/RPA, Product Engineering &amp; Digital Transformation</div>
  <div class="legend" style="left:611px;width:120px"><div class="k"><i style="background:var(--pink)"></i><span style="color:var(--pink)">5%</span></div>Campaigns on Events Audience Acquisition</div>
  <svg class="abs pie" width="340" height="340" viewBox="0 0 320 320">
    <path d="M50 160A110 110 0 0 1 160 50L160 100A60 60 0 0 0 100 160Z" fill="#27aee0"/>
    <path d="M160 25A135 135 0 0 1 295 160L220 160A60 60 0 0 0 160 100Z" fill="#3fd8be"/>
    <path d="M270 160A110 110 0 0 1 160 270L160 220A60 60 0 0 0 220 160Z" fill="#f1306e"/>
    <path d="M160 270A110 110 0 0 1 50 160L100 160A60 60 0 0 0 160 220Z" fill="#fbbd12"/>
    <circle cx="160" cy="160" r="60" fill="#3d4550"/>
    <circle cx="160" cy="160" r="42" fill="#fff"/>
    <g font-family="Roboto,sans-serif" font-weight="500" fill="#fff" fill-opacity=".45">
      <text x="98" y="102" font-size="18">50%</text>
      <text x="225" y="100" font-size="22">75%</text>
      <text x="92" y="228" font-size="15">20%</text>
      <text x="218" y="228" font-size="13">5%</text>
    </g>
  </svg>
</section>

<section class="abs blogs">
  <h2 class="h-red">Blogs</h2>
  <a class="view btn-line">View All <svg width="10" height="8" viewBox="0 0 10 8" fill="none" stroke="#333"><path d="M0 4h9M6 1l3 3-3 3"/></svg></a>
  <div class="post" style="left:133px">
    <div class="ph" role="img" aria-label="Hand holding a yellow funnel over banknotes" style="background:linear-gradient(135deg,#e8e6e2,#c9c2b0 55%,#8a7a4a)"></div>
    <h3>Sales Cadence Elements That Can Turn Your Sales Game</h3>
    <a class="btn-line">Read More</a>
  </div>
  <div class="post" style="left:451px">
    <div class="ph" role="img" aria-label="Hand holding a megaphone on a yellow background" style="background:linear-gradient(135deg,#fbd94a,#f5c518 60%,#e8b60f)"></div>
    <h3>Achieving Sales Target Through The Re-ferral Road</h3>
    <a class="btn-line">Read More</a>
  </div>
  <div class="post" style="left:769px">
    <div class="ph" role="img" aria-label="Football goalkeeper diving in a floodlit stadium" style="background:linear-gradient(160deg,#1b2a44,#3a5276 50%,#2f5a2e)"></div>
    <h3>Getting Past The Gatekeeper: An Art To Master</h3>
    <a class="btn-line">Read More</a>
  </div>
</section>

<div class="abs foot-bg"></div>
<div class="abs form">
  <h2>Let's Get Started</h2>
  <div class="fld" style="left:20px;top:83px;width:218px">Name</div>
  <div class="fld" style="left:251px;top:83px;width:218px">Email</div>
  <div class="fld" style="left:20px;top:134px;width:218px">Phone</div>
  <div class="fld" style="left:251px;top:134px;width:218px">Select Courier Type<svg width="8" height="5" viewBox="0 0 8 5"><path d="M0 0h8L4 5z" fill="#888"/></svg></div>
  <div class="fld" style="left:20px;top:185px;width:449px;height:93px;align-items:flex-start;padding-top:12px">Message</div>
  <a class="btn-red">Submit</a>
</div>
<div class="abs map" role="img" aria-label="Street map showing the office location and nearby businesses"></div>

<div class="fbrand"><span class="sq"></span>PalvorIntel</div>
<p class="fabout">Lorem Ipsum is simply dummy text of the printing and...</p>
<div class="fsocial"><i class="dot"></i><i class="dot"></i><i class="dot"></i><i class="dot"></i></div>
<div class="fcol" style="left:291px"><h4>Quick Link</h4><ul><li class="on">Home</li><li>Shop</li><li>Faq</li><li>Contct Us</li><li>Privacy Policy</li><li>Terms of Use</li></ul></div>
<div class="fcol" style="left:471px"><h4>Services</h4><ul><li>B2B Appointment Setting</li><li>Account Based Marketing</li><li>Research As A Service</li><li>Event / Webinar Management</li><li>Staffing &amp; Talent Acquisition</li><li>Digital Marketing</li><li>Social Media Research</li><li>Lead Nurturing</li></ul></div>
<div class="fcol" style="left:689px"><h4>Library</h4><ul><li>Videos</li><li>Infographics</li><li>Blog</li><li>Case Studies</li></ul></div>
<div class="fcol" style="left:849px;width:220px">
  <h4>Contact info</h4>
  <div class="crow"><svg width="14" height="18" viewBox="0 0 14 18"><path d="M7 0a7 7 0 0 1 7 7c0 5-7 11-7 11S0 12 0 7a7 7 0 0 1 7-7z" fill="#ddd"/><circle cx="7" cy="7" r="2.5" fill="#262626"/></svg><span style="line-height:17px">Unit 12 Harbour Point Commerce Lane, Eastvale 4, Marlow Bay</span></div>
  <div class="crow"><svg width="14" height="14" viewBox="0 0 12 12"><path d="M2 1l2.5 0 1 3-1.5 1a6 6 0 0 0 3 3l1-1.5 3 1v2.5A1 1 0 0 1 10 11 9 9 0 0 1 1 2a1 1 0 0 1 1-1z" fill="#ddd"/></svg>555.214.7730</div>
  <div class="crow"><svg width="14" height="12" viewBox="0 0 12 10"><rect x="0.5" y="0.5" width="11" height="9" fill="none" stroke="#ddd"/><path d="M1 1l5 4 5-4" stroke="#ddd" fill="none"/></svg>info@palvorintel.com</div>
</div>
<div class="abs copy">Copyright © 2020 PalvorIntel. All Rights Reserved</div>

</body>
</html>
```